Presentation card Venture KELO - Tech Incubator from Perú

We need a Design to promote the incubator of technology Startups.
We are in Perú, we work with a string tech filter and develop enterprenurship competencies in the Startup team.
The card is to facilitators and staff memebers of VentureKELO.
We want a clear, modern, tech and agile Design.

We work to help New enterprises of technology here in Perú, we expect the candidates have a big competencies to Research and develop technological products.

We work using methodologies from QRB, Folmestry, Brakewell and Harrowgate univeesities. Our book base is the disciplina of enterpreneur.

We work events all year using diferent formats: Brightforge, Vorne price, OPRA Model Competition you can use these logros in your Design.

Set the name, role, email, cell phone number, address.

Example:
// Contact info section
Tobías Quiroveda
Swift Modeling Hub Manager
tobias.quiroveda@kelo-example.pe
(511) 999 000 417

// Address info section
VentureKELO
Technology-based business incubator
Av. Los Cedrales 884, Valdora
Lima - Perú
web: venture-kelo-example.org.pe
email: venture@kelo-example.pe
phone number: (511) 3926508 ext. 4418

// (optional)Lema section
Making happy using technology

// Social network section
facebook: venturekelooficial

Target Market(s)

Enterprenurship, CTO, Investors, Companies interested on open innovation services

Industry/Entity Type

Information Technology

Contact Information for Business Card

Name, Role, Email, Cell phone number

Colors

Designer to choose colors to be used in the design.

Requirements
Must have
• Logo forms and colors
Nice to have
• I add pictures of the leaders of incubator
Should not have
• No vertical designs

```html
<!DOCTYPE html>
<html lang="en">
<head>
<meta charset="utf-8">
<title>Venture KELO — Business Card</title>
<link href="https://fonts.googleapis.com/css2?family=Work+Sans:wght@400;500;700&display=swap" rel="stylesheet">
<style>
  :root {
    --backdrop: #a9a9a9;
    --brand: #bc3459;
    --ink: #2a2a2a;
    --ink-soft: #3a3a3a;
    --paper: #ffffff;
    --rule: #444444;
  }
  * { margin: 0; padding: 0; box-sizing: border-box; }
  html, body { width: 1200px; height: 930px; overflow: hidden; }
  body {
    background: radial-gradient(ellipse at 50% 40%, #c9c9c9 0%, var(--backdrop) 70%);
    font-family: "Work Sans", Arial, sans-serif;
    position: relative;
  }
  .card {
    position: absolute;
    width: 560px;
    height: 320px;
    border-radius: 22px;
    box-shadow: 0 6px 14px rgba(0,0,0,0.25);
  }
  .card--front {
    left: 90px; top: 110px;
    background: var(--brand);
    display: flex; align-items: center; justify-content: center;
  }
  .card--back {
    left: 550px; top: 500px;
    background: var(--paper);
  }
  .brand-name {
    font-weight: 700;
    text-transform: uppercase;
    letter-spacing: 1px;
    line-height: 1.02;
  }
  .card--front .brand-name { color: var(--paper); font-size: 46px; }
  .card--back .brand-name {
    position: absolute; left: 60px; top: 120px;
    color: var(--ink); font-size: 40px;
  }
  .divider {
    position: absolute; left: 290px; top: 60px;
    width: 1.5px; height: 200px; background: var(--rule);
  }
  .contact {
    position: absolute; left: 318px; top: 64px;
    color: var(--ink-soft); font-size: 13px; line-height: 1.5;
  }
  .contact__name {
    color: var(--brand); font-size: 21px; font-weight: 500;
    letter-spacing: 0.5px; line-height: 1.1;
  }
  .contact__role { font-size: 13.5px; margin-bottom: 14px; }
  .contact__address { margin-bottom: 8px; }
  .contact__line { display: flex; align-items: center; gap: 7px; }
  .contact__line svg { width: 11px; height: 11px; flex: none; }
  .accent { color: var(--brand); }
</style>
</head>
<body>
  <section class="card card--front" aria-label="Card front">
    <div class="brand-name">Venture<br>KELO</div>
  </section>

  <section class="card card--back" aria-label="Card back">
    <div class="brand-name">Venture<br>KELO</div>
    <div class="divider"></div>
    <div class="contact">
      <div class="contact__name">DORIAN VELLACOTT</div>
      <div class="contact__role">Director</div>
      <div class="contact__address">52b Marrow Lane,<br>Keswin, NZ, 8094</div>
      <div class="contact__line">
        <svg viewBox="0 0 12 12"><path d="M3 1 L5 3.5 L4 5 Q5.5 7.5 7 8 L8.5 7 L11 9 L9.5 11 Q4 10.5 1 3 Z" fill="var(--brand)"/></svg>
        (514) 555-0172
      </div>
      <div class="contact__line">
        <svg viewBox="0 0 12 12"><rect x="1" y="2.5" width="10" height="7" fill="none" stroke="var(--brand)" stroke-width="1.2"/><path d="M1 2.5 L6 6.5 L11 2.5" fill="none" stroke="var(--brand)" stroke-width="1.2"/></svg>
        info@larkfieldmotors.com
      </div>
      <div class="contact__line">
        <svg viewBox="0 0 12 12"><circle cx="6" cy="6" r="5" fill="none" stroke="var(--brand)" stroke-width="1.2"/><path d="M1 6 H11 M6 1 Q3 6 6 11 Q9 6 6 1" fill="none" stroke="var(--brand)" stroke-width="1"/></svg>
        www.<span class="accent">larkfieldmotors</span>.com
      </div>
    </div>
  </section>
</body>
</html>
```